Neue Verpackung für unsere Arbeitssocken :) | New packaging for our work socks :)
Zielgruppe
Wir sind eine Modefirma und suchen ein hochwertiges Design für unsere Arbeitssocken, unsere Zielgruppe sind Männer und Frauen.
We are a fashion company and looking for a high quality design for our work socks, our target group are men and women.
Aufgabenstellung
Die Datei 'cintas brunsdorff' zeigt unser jetziges Design. Das neue Design soll in Richtung der DUX Arbeitssocken gehen!
Logo, Texte und Farben können abgewandelt werden.
The file 'cintas brunsdorff' shows our current design. The new design should go in the direction of the DUX work socks!
Logo, texts and colors can be modified.

```html
<!DOCTYPE html>
<html lang="de">
<head>
<meta charset="utf-8">
<title>Brunsdorff Arbeitssocken – Banderole</title>
<link rel="stylesheet" href="https://fonts.googleapis.com/css2?family=Montserrat:wght@300;400;700;800;900&display=swap">
<style>
  :root {
    --yellow: #ffc400;
    --black: #0d0d0d;
    --white: #ffffff;
    --stage: #e4e4e4;
    --ink-soft: #2a2a2a;
  }
  * { margin: 0; padding: 0; box-sizing: border-box; }
  html, body { width: 1200px; height: 1080px; overflow: hidden; }
  body {
    background: var(--stage);
    font-family: "Montserrat", sans-serif;
    color: var(--black);
    position: relative;
  }
  .band {
    position: absolute;
    left: 47px;
    width: 1115px;
    height: 293px;
    background: var(--yellow);
    box-shadow: 0 4px 10px rgba(0,0,0,0.18);
  }
  .band--back { top: 149px; }
  .band--front { top: 606px; }
  .band__strip {
    position: absolute;
    left: 0; right: 0; bottom: 0;
    height: 70px;
    background: var(--black);
    border-top: 5px solid var(--white);
  }
  .wordmark {
    position: absolute;
    width: 282px;
    font-weight: 900;
    font-size: 42px;
    line-height: 1;
    letter-spacing: -1.5px;
    text-align: center;
    color: var(--black);
  }
  .pack-count {
    position: absolute;
    width: 120px;
    margin-left: -60px;
    top: 10px;
    font-weight: 900;
    font-size: 23px;
    text-align: center;
    line-height: 1;
  }
  .seal {
    position: absolute;
    width: 110px;
    margin-left: -55px;
    top: 72px;
    text-align: center;
  }
  .seal__dot {
    display: block;
    width: 60px; height: 60px;
    margin: 0 auto 8px;
    border-radius: 50%;
    background: var(--black);
  }
  .seal__name {
    font-weight: 800;
    font-size: 13px;
    letter-spacing: 0.5px;
  }
  .features {
    position: absolute;
    left: 147px;
    top: 96px;
    width: 283px;
    display: grid;
    grid-template-columns: 1fr 1fr;
    row-gap: 9px;
  }
  .feature__de { font-weight: 800; font-size: 11px; line-height: 12px; white-space: nowrap; }
  .feature__en { font-weight: 300; font-size: 11px; line-height: 12px; color: var(--ink-soft); }
  .feature--right { text-align: right; }
  .cert-badge {
    position: absolute;
    left: 147px; top: 13px;
    width: 74px; height: 51px;
    background: var(--white);
  }
  .composition {
    position: absolute;
    right: 685px; top: 11px;
    font-size: 7px;
    line-height: 9px;
    text-align: right;
    color: var(--white);
  }
  .composition b { font-weight: 700; }
  .care {
    position: absolute;
    left: 338px; top: 38px;
    width: 92px; height: 22px;
  }
  .size-tag {
    position: absolute;
    width: 120px;
    margin-left: -60px;
    top: 7px;
    text-align: center;
    line-height: 1;
  }
  .size-tag__name { font-weight: 900; font-size: 18px; color: var(--yellow); line-height: 18px; }
  .size-tag__size { font-weight: 800; font-size: 15px; color: var(--white); margin-top: 3px; }
  .size-main {
    position: absolute;
    left: 645px; top: 11px;
    line-height: 1;
  }
  .size-main__name { font-weight: 900; font-size: 23px; color: var(--yellow); letter-spacing: 0.5px; }
  .size-main__size { font-weight: 800; font-size: 21px; color: var(--white); margin-top: 10px; }
</style>
</head>
<body>

<!-- Rückseite mit Produktmerkmalen -->
<section class="band band--back">
  <div class="wordmark" style="left:147px;top:26px;">BRUNSDORFF</div>

  <div class="features">
    <div class="feature"><div class="feature__de">POLSTERND</div><div class="feature__en">padding effect</div></div>
    <div class="feature feature--right"><div class="feature__de">WASCHMASCHIENENFEST</div><div class="feature__en">machine washable</div></div>
    <div class="feature"><div class="feature__de">STRAPAZIERFÄHIG</div><div class="feature__en">hard-wearing</div></div>
    <div class="feature feature--right"><div class="feature__de">SCHWEIßAUFSAUGEND</div><div class="feature__en">sweat-absorbing</div></div>
    <div class="feature"><div class="feature__de">KORREKTE PASSFORM</div><div class="feature__en">perfect fit</div></div>
    <div class="feature feature--right"><div class="feature__de">HAUTSYMPATHISCH</div><div class="feature__en">pleasant on the skin</div></div>
  </div>

  <div class="pack-count" style="left:534px;">3 PAAR</div>
  <div class="seal" style="left:534px;"><span class="seal__dot"></span><div class="seal__name">BRUNSDORFF</div></div>

  <div class="wordmark" style="left:646px;top:92px;">BRUNSDORFF</div>

  <div class="pack-count" style="left:1034px;">3 PAAR</div>
  <div class="seal" style="left:1034px;"><span class="seal__dot"></span><div class="seal__name">BRUNSDORFF</div></div>

  <div class="band__strip">
    <div class="cert-badge" role="img" aria-label="Zertifikatssiegel"></div>
    <div class="composition"><b>70%</b> BAUMWOLLE / COTTON<br>COTON / KATOEN / BAVLNY<br><b>30%</b> POLYESTER</div>
    <svg class="care" viewBox="0 0 92 22" fill="none" stroke="#fff" stroke-width="1.3" aria-label="Pflegesymbole">
      <path d="M1 5 L3 20 H16 L18 5"/><path d="M1 5 q4 3 8.5 0 q4.5 3 8.5 0"/>
      <text x="9.5" y="17" font-size="7" fill="#fff" stroke="none" text-anchor="middle" font-family="Montserrat, sans-serif" font-weight="700">60°</text>
      <path d="M23 20 L31 3 L39 20 Z"/><path d="M23 3 L39 20 M39 3 L23 20"/>
      <rect x="44" y="3" width="17" height="17"/><circle cx="52.5" cy="11.5" r="6"/><path d="M44 3 L61 20 M61 3 L44 20"/>
      <path d="M65 20 L67 8 H80 L83 20 Z"/><path d="M65 8 L83 20 M83 8 L65 20"/>
      <circle cx="83" cy="11.5" r="0" /><circle cx="82" cy="11.5" r="0"/>
      <circle cx="83.5" cy="11.5" r="0"/>
      <circle cx="82.5" cy="11.5" r="0"/>
      <circle cx="83" cy="11.5" r="0"/>
      <circle cx="83" cy="11.5" r="0"/>
      <circle cx="83" cy="11.5" r="0"/>
    </svg>
    <div class="size-tag" style="left:534px;"><div class="size-tag__name">ARBEITS<br>SOCKEN</div><div class="size-tag__size">43-46</div></div>
    <div class="size-main"><div class="size-main__name">ARBEITS SOCKEN</div><div class="size-main__size">EU 43-46</div></div>
    <div class="size-tag" style="left:1034px;"><div class="size-tag__name">ARBEITS<br>SOCKEN</div><div class="size-tag__size">43-46</div></div>
  </div>
</section>

<!-- Vorderseite -->
<section class="band band--front">
  <div class="wordmark" style="left:147px;top:92px;">BRUNSDORFF</div>

  <div class="pack-count" style="left:534px;">3 PAAR</div>
  <div class="seal" style="left:534px;"><span class="seal__dot"></span><div class="seal__name">BRUNSDORFF</div></div>

  <div class="wordmark" style="left:646px;top:92px;">BRUNSDORFF</div>

  <div class="pack-count" style="left:1034px;">3 PAAR</div>
  <div class="seal" style="left:1034px;"><span class="seal__dot"></span><div class="seal__name">BRUNSDORFF</div></div>

  <div class="band__strip">
    <div class="cert-badge" role="img" aria-label="Zertifikatssiegel"></div>
    <div class="composition"><b>70%</b> BAUMWOLLE / COTTON<br>COTON / KATOEN / BAVLNY<br><b>30%</b> POLYESTER</div>
    <svg class="care" viewBox="0 0 92 22" fill="none" stroke="#fff" stroke-width="1.3" aria-label="Pflegesymbole">
      <path d="M1 5 L3 20 H16 L18 5"/><path d="M1 5 q4 3 8.5 0 q4.5 3 8.5 0"/>
      <text x="9.5" y="17" font-size="7" fill="#fff" stroke="none" text-anchor="middle" font-family="Montserrat, sans-serif" font-weight="700">60°</text>
      <path d="M23 20 L31 3 L39 20 Z"/><path d="M23 3 L39 20 M39 3 L23 20"/>
      <rect x="44" y="3" width="17" height="17"/><circle cx="52.5" cy="11.5" r="6"/><path d="M44 3 L61 20 M61 3 L44 20"/>
      <path d="M65 20 L67 8 H80 L83 20 Z"/><path d="M65 8 L83 20 M83 8 L65 20"/>
    </svg>
    <div class="size-tag" style="left:534px;"><div class="size-tag__name">ARBEITS<br>SOCKEN</div><div class="size-tag__size">43-46</div></div>
    <div class="size-main"><div class="size-main__name">ARBEITS SOCKEN</div><div class="size-main__size">EU 43-46</div></div>
    <div class="size-tag" style="left:1034px;"><div class="size-tag__name">ARBEITS<br>SOCKEN</div><div class="size-tag__size">43-46</div></div>
  </div>
</section>

</body>
</html>
```